Nova crest cleansers Trading L.L.C

We need stationary design for our new company contain ( Business card - head latter - envelops( big & small) - folder file ) One identity and creative design & has related with logo colors ....A unified identity
The main elements of the design that includes the main logos (logo crest + crest logo membership Khalid bin Nasser) as it is in the attachment then the address of the company.
The Address is
Ras Hamdan - Next to Corniche Plaza Mall
Noor Trade Tower Building - 604
P.O.Box : 47819 Dubai - U.A.E
Tel. : 00971 4 58 71 204
Fax : 00971 4 58 71 205
Email : info@novacrestcleansers.example
www.novacrestcleansers.example
Please read the attachment in an important way, especially the terms of the government logo (Khalid Bin Nasser Membership)
In the design of business cards .. Please put slogans (Oru fresh home - Oru Professional - Faraheed ) be in the back of the card
Put my name sample
Samir Youssef Abdul Karim
Director Manager
Mobil : + 971 52 387 0 387

```html
<!DOCTYPE html>
<html lang="en">
<head>
<meta charset="utf-8">
<title>Nova crest cleansers Trading L.L.C – Business Card</title>
<link rel="stylesheet" href="https://fonts.googleapis.com/css2?family=Lato:wght@400;700;900&display=swap">
<style>
  :root {
    --stage: #2a2a2a;
    --red: #e32028;
    --red-dark: #c5141c;
    --red-light: #f0373e;
    --white: #ffffff;
    --paper: #f4f4f4;
    --ink: #2b2b2b;
    --grey: #8a8a8a;
    --green: #1e8a3c;
  }
  * { box-sizing: border-box; margin: 0; padding: 0; }
  html, body { width: 1200px; height: 896px; overflow: hidden; }
  body {
    background: var(--stage);
    font-family: "Lato", sans-serif;
    position: relative;
  }
  .card {
    position: absolute;
    width: 540px;
    height: 310px;
    border-radius: 18px;
    overflow: hidden;
  }

  /* Back side */
  .card-back {
    left: 50px; top: 110px;
    background: linear-gradient(135deg, var(--red-light) 0%, var(--red) 55%, var(--red-dark) 100%);
    color: var(--white);
  }
  .card-back .membership {
    position: absolute;
    left: 40px; top: 100px;
    width: 320px;
  }
  .membership .est {
    font-size: 13px; font-weight: 700; letter-spacing: 1px;
    line-height: 1.35;
  }
  .membership .mark {
    margin-top: 8px;
    font-size: 30px; font-weight: 900; letter-spacing: 0.5px;
    line-height: 1.15;
  }
  .card-back .brand-strip {
    position: absolute;
    right: 0; top: 0; bottom: 0;
    width: 150px;
    background: var(--white);
    display: flex; flex-direction: column; justify-content: center; align-items: flex-start;
    padding-left: 16px;
    gap: 14px;
  }
  .brand-strip .brand {
    display: flex; align-items: center; gap: 6px;
    font-size: 13px; font-weight: 900; color: var(--green);
    white-space: nowrap;
  }
  .brand-strip .brand::before {
    content: ""; width: 10px; height: 10px; background: var(--green);
  }

  /* Front side */
  .card-front {
    left: 610px; top: 476px;
    background: linear-gradient(160deg, var(--white) 0%, var(--paper) 100%);
    color: var(--ink);
  }
  .card-front .edge {
    position: absolute; left: 0; right: 0; bottom: 0; height: 14px;
    background: var(--red);
  }
  .card-front .membership {
    position: absolute; left: 30px; top: 28px; color: var(--ink);
  }
  .card-front .membership .est { font-size: 11px; }
  .card-front .membership .mark { font-size: 22px; color: var(--red); margin-top: 4px; }
  .holder {
    position: absolute; left: 30px; top: 118px;
    border-left: 2px solid var(--red);
    padding-left: 12px;
  }
  .holder .name { font-size: 20px; font-weight: 700; color: var(--red); white-space: nowrap; }
  .holder .role { font-size: 14px; margin-top: 2px; }
  .contacts {
    position: absolute; left: 30px; top: 186px;
    list-style: none; font-size: 12px; line-height: 1.55;
  }
  .contacts li { display: flex; align-items: center; gap: 8px; white-space: nowrap; }
  .contacts svg { width: 11px; height: 11px; fill: var(--red); flex: none; }
  .divider {
    position: absolute; left: 300px; top: 180px; width: 1px; height: 100px;
    background: var(--grey);
  }
  .address {
    position: absolute; left: 312px; top: 186px;
    font-size: 11px; line-height: 1.6; font-style: normal;
    white-space: nowrap;
  }
  .address svg { width: 14px; height: 16px; fill: var(--red); display: block; margin-bottom: 6px; }
</style>
</head>
<body>

<section class="card card-back" aria-label="Business card back">
  <div class="membership">
    <p class="est">Khalid Bin Nasser Est.<br>for SME Development</p>
    <p class="mark">Khalid Bin Nasser<br>Membership</p>
  </div>
  <div class="brand-strip">
    <p class="brand">Oru fresh home</p>
    <p class="brand">Oru Professional</p>
  </div>
</section>

<section class="card card-front" aria-label="Business card front">
  <div class="membership">
    <p class="est">Khalid Bin Nasser Est. for SME Development</p>
    <p class="mark">Khalid Bin Nasser Membership</p>
  </div>

  <div class="holder">
    <p class="name">Samir Youssef Abdul Karim</p>
    <p class="role">Director Manager</p>
  </div>

  <ul class="contacts">
    <li><svg viewBox="0 0 10 10"><rect x="2.5" y="0" width="5" height="10" rx="1"/></svg>: + 971 52 387 0 387</li>
    <li><svg viewBox="0 0 10 10"><path d="M2 0h2l1 3-1.5 1a6 6 0 0 0 2.5 2.5L7 5l3 1v2a2 2 0 0 1-2 2A8 8 0 0 1 0 2a2 2 0 0 1 2-2z"/></svg>: 00971 4 58 71 204</li>
    <li><svg viewBox="0 0 10 10"><rect x="0" y="3" width="10" height="6" rx="1"/><rect x="2" y="0" width="6" height="3"/></svg>: 00971 4 58 71 205</li>
    <li><svg viewBox="0 0 10 10"><path d="M0 2h10v6H0z M0 2l5 4 5-4"/></svg>: info@novacrestcleansers.example</li>
    <li><svg viewBox="0 0 10 10"><circle cx="5" cy="5" r="5"/></svg>: www.novacrestcleansers.example</li>
  </ul>

  <div class="divider"></div>

  <address class="address">
    <svg viewBox="0 0 14 16"><path d="M7 0a6 6 0 0 1 6 6c0 4-6 10-6 10S1 10 1 6a6 6 0 0 1 6-6zm0 3.5a2.5 2.5 0 1 0 0 5 2.5 2.5 0 0 0 0-5z"/></svg>
    Ras Hamdan - Next to Corniche Plaza Mall<br>
    Noor Trade Tower Building - 604<br>
    P.O.Box : 47819 Dubai - U.A.E
  </address>

  <div class="edge"></div>
</section>

</body>
</html>
```